Business card design needed

i am a small sized carpentry business looking to generate work in decks, pergolas, small renovations including bathroom renovations or overseeing new homes being built.

Carpentry

R K Carpentry
Marcus Ellery
0417382906
Specialize in quality decks, pergolas, small renovations including bathrooms and housing project management.
FREE QUOTES

```html
<!DOCTYPE html>
<html lang="en">
<head>
<meta charset="utf-8">
<title>R K Carpentry – Business Card</title>
<link rel="stylesheet" href="https://fonts.googleapis.com/css2?family=Arimo:wght@400;500;600&display=swap">
<style>
  :root {
    --backdrop: #e9e7e3;
    --card: #ffffff;
    --ink: #161612;
    --shadow: rgba(0, 0, 0, 0.18);
  }
  * { margin: 0; padding: 0; box-sizing: border-box; }
  html, body {
    width: 1200px;
    height: 879px;
    overflow: hidden;
    background: var(--backdrop);
    font-family: "Arimo", Arial, sans-serif;
    color: var(--ink);
  }
  .business-card {
    position: absolute;
    left: 360px;
    top: 50px;
    width: 480px;
    height: 780px;
    background: var(--card);
    box-shadow: 0 6px 18px var(--shadow);
  }
  .company-name {
    position: absolute;
    top: 36px;
    right: 34px;
    font-size: 46px;
    font-weight: 500;
    letter-spacing: 0.5px;
    white-space: nowrap;
  }
  .contact {
    position: absolute;
    left: 34px;
    top: 330px;
  }
  .contact-name {
    font-size: 40px;
    font-weight: 400;
    line-height: 1;
    letter-spacing: 0.5px;
  }
  .contact-phone {
    margin-top: 6px;
    font-size: 30px;
    font-weight: 400;
    line-height: 1;
    letter-spacing: 0.5px;
  }
  .services {
    position: absolute;
    left: 34px;
    right: 30px;
    top: 500px;
    font-size: 17px;
    line-height: 1.45;
    list-style: none;
  }
  .services-row { white-space: nowrap; }
  .services .divider {
    display: inline-block;
    width: 3px;
    height: 17px;
    margin: 0 8px;
    vertical-align: -2px;
    background: var(--ink);
  }
  .services-row.secondary { padding-left: 0; }
  .offer {
    position: absolute;
    left: 30px;
    bottom: 48px;
    font-size: 60px;
    font-weight: 600;
    letter-spacing: 1px;
    line-height: 1;
    white-space: nowrap;
  }
</style>
</head>
<body>
  <main class="business-card">
    <h1 class="company-name">R K Carpentry</h1>

    <section class="contact">
      <p class="contact-name">Marcus Ellery</p>
      <p class="contact-phone">0417382906</p>
    </section>

    <ul class="services">
      <li class="services-row">Quality Decks<span class="divider"></span>Pergolas<span class="divider"></span>Small Renovations</li>
      <li class="services-row secondary">Bathrooms<span class="divider"></span>Housing Project Management</li>
    </ul>

    <p class="offer">FREE QUOTES</p>
  </main>
</body>
</html>
```